Video Production Company Website

A video production company website for "Quiet Fern Studios"
Home page must have video player and way to select between 3 different videos.

Company does video Post production : Editing, Motion Graphics, Color correction, and Aerial videography

Design should be simple but Pro looking..

Earthy color palette with slight texture..

Industry/Entity Type

Film Production

Number of Pages Required

3 page

Font styles to use
Sans Serif
Other font styles liked:

Requirements
Nice to have
• Thumbnails on homepage to past project clips
Should not have
• full page video

```html
<!DOCTYPE html>
<html lang="en">
<head>
<meta charset="utf-8">
<title>Quiet Fern Studios</title>
<link href="https://fonts.googleapis.com/css2?family=Oswald:wght@400;500;700&family=Open+Sans:wght@400;600;700&display=swap" rel="stylesheet">
<style>
:root{
  --ink-deep:#0f3634;
  --teal-dark:#154a47;
  --teal-mid:#1f625d;
  --teal:#2f8f86;
  --teal-bright:#4fc2b0;
  --red:#d63b27;
  --paper:#ffffff;
  --grey-card:#e9ebea;
  --text-light:#e6f2f0;
  --text-dark:#333;
}
*{box-sizing:border-box;margin:0;padding:0}
html,body{width:1200px;height:2332px;overflow:hidden}
body{background:var(--teal-dark);font-family:"Open Sans",Arial,sans-serif;color:var(--text-light);position:relative}
.display{font-family:"Oswald","Arial Narrow",sans-serif;text-transform:uppercase}

/* header */
.site-header{position:absolute;top:0;left:0;width:1200px;height:80px;background:var(--ink-deep);border-bottom:4px solid var(--teal)}
.brand{position:absolute;left:24px;top:0;height:76px;display:flex;align-items:center;gap:12px}
.brand-mark{width:16px;height:16px;background:var(--teal-bright)}
.brand-name{font-family:"Open Sans",Arial,sans-serif;font-weight:600;font-size:28px;color:var(--paper)}
.main-nav{position:absolute;right:26px;top:24px;display:flex;gap:26px}
.main-nav a{font-family:"Oswald",sans-serif;font-size:20px;color:var(--red);text-decoration:none;text-transform:uppercase}
.main-nav a.active{color:var(--paper);border-bottom:2px solid var(--paper)}

/* hero */
.hero{position:absolute;top:84px;left:0;width:1200px;height:536px}
.hero-media{position:absolute;inset:0;background:linear-gradient(120deg,#5c6a3a 0%,#8c8a4f 35%,#b9a36a 55%,#6f7a45 80%,#3e4a2a 100%)}
.hero-dots{position:absolute;top:56px;left:540px;display:flex;gap:10px}
.hero-dots span{width:18px;height:18px;background:#888}
.hero-dots span:nth-child(2){background:var(--red)}
.hero-dots span:nth-child(3){background:var(--teal-bright)}
.hero-dots span:nth-child(4){background:var(--paper)}
.hero-arrow{position:absolute;top:288px;width:48px;height:48px;border-radius:50%;background:rgba(255,255,255,.85)}
.hero-arrow.prev{left:16px}.hero-arrow.next{right:16px}
.featured{position:absolute;left:580px;top:236px;width:520px;height:254px;background:rgba(255,255,255,.93);color:var(--text-dark);padding:0 22px}
.featured-head{display:flex;justify-content:space-between;align-items:center;height:62px;border-bottom:2px solid #ccc}
.featured-head h2{font-size:34px;color:var(--red);font-weight:500}
.tag{font-family:"Oswald",sans-serif;font-size:18px;color:#777;text-transform:uppercase;background:#e4e4e4;padding:2px 10px}
.featured p{font-size:13px;line-height:18px;margin-top:12px}

/* thumbnails */
.thumb-band{position:absolute;top:620px;left:0;width:1200px;height:380px;background:repeating-linear-gradient(45deg,#c3c5c5 0 3px,#cdd0cf 3px 6px)}
.thumb-card{position:absolute;top:52px;width:340px;height:244px;background:var(--grey-card);border:2px solid var(--paper);padding:10px}
.thumb-card h3{font-size:26px;color:var(--red);font-weight:500;text-align:center;height:38px}
.thumb-media{height:178px}
.chevron{position:absolute;top:920px;left:0;width:1200px;height:100px}

/* service sections */
.section-label{position:absolute;left:0;width:1200px;height:50px;background:var(--teal-mid);border-top:3px solid var(--teal);display:flex;align-items:center}
.section-label h2{background:var(--paper);color:var(--red);font-size:26px;font-weight:500;height:100%;display:flex;align-items:center;padding:0 52px 0 24px;clip-path:polygon(0 0,100% 0,90% 100%,0 100%)}
.service{position:absolute;left:24px;width:1152px;height:284px;display:flex;gap:16px}
.service-body{flex:1;background:var(--teal);padding:14px 22px;position:relative}
.service-body.bordered{border:2px solid var(--text-light)}
.service-head{display:flex;justify-content:space-between;align-items:center;border-bottom:1px solid rgba(255,255,255,.4);padding-bottom:8px}
.service-head h3{font-size:27px;font-weight:700;color:var(--paper)}
.service-head .project{font-family:"Oswald",sans-serif;font-size:22px;color:var(--teal-bright);text-transform:uppercase;background:rgba(0,0,0,.12);padding:0 8px}
.service-body p{font-size:12.5px;line-height:17px;margin-top:10px}
.more{position:absolute;right:22px;bottom:12px;font-size:14px;color:var(--paper);text-decoration:underline}
.service-media{width:370px;height:284px;border:3px solid var(--text-light)}

/* footer */
.site-footer{position:absolute;top:2140px;left:0;width:1200px;height:192px;background:var(--ink-deep);border-top:4px solid var(--teal)}
.footer-nav{position:absolute;left:30px;top:40px;display:flex;gap:34px}
.footer-nav a{font-family:"Oswald",sans-serif;font-size:18px;color:var(--paper);text-decoration:none;text-transform:uppercase}
.footer-nav a.active{border-bottom:2px solid var(--paper)}
.social{position:absolute;right:36px;top:28px;display:flex;gap:8px}
.social span{width:36px;height:36px;background:var(--teal-mid);border:1px solid var(--text-light)}
.newsletter{position:absolute;right:36px;top:80px;width:280px}
.newsletter h4{font-size:12px;color:var(--paper);text-transform:uppercase;margin-bottom:6px}
.newsletter-row{display:flex}
.newsletter-row span{flex:1;height:28px;background:var(--paper);color:#999;font-size:12px;padding:6px}
.newsletter-row b{width:60px;height:28px;background:var(--teal);color:var(--paper);font-family:"Oswald",sans-serif;font-weight:400;font-size:16px;text-align:center;line-height:28px}
.legal{position:absolute;bottom:14px;width:100%;text-align:center;font-size:13px;color:var(--paper)}
.legal small{display:block;font-size:11px;color:#a9c6c2}
</style>
</head>
<body>

<header class="site-header">
  <div class="brand"><span class="brand-mark"></span><span class="brand-name">Quiet Fern</span></div>
  <nav class="main-nav">
    <a class="active" href="#">Home</a><a href="#">About Us</a><a href="#">Films</a><a href="#">Services</a><a href="#">News &amp; Events</a><a href="#">Contact Us</a>
  </nav>
</header>

<section class="hero">
  <div class="hero-media" role="img" aria-label="Aerial footage of a road running between farm fields and forest"></div>
  <div class="hero-dots"><span></span><span></span><span></span><span></span></div>
  <svg class="hero-arrow prev" viewBox="0 0 48 48"><path d="M28 14 L18 24 L28 34" fill="none" stroke="#154a47" stroke-width="4"/></svg>
  <svg class="hero-arrow next" viewBox="0 0 48 48"><path d="M20 14 L30 24 L20 34" fill="none" stroke="#154a47" stroke-width="4"/></svg>
  <div class="featured">
    <div class="featured-head"><h2 class="display">Featured Heading</h2><span class="tag">Project Title</span></div>
    <p>Our crew captured this valley from above over three quiet mornings. Every pass was planned with the farmers, timed to the light and flown low over the tree line. The final cut blends drone footage with ground shots and a warm grade that keeps the earthy tones of the fields.</p>
    <p>Watch the full reel to see how we shape raw flight footage into a calm and steady story. Continue to the films page for the complete series.</p>
  </div>
</section>

<section class="thumb-band">
  <article class="thumb-card" style="left:40px">
    <h3 class="display">Post-Production</h3>
    <div class="thumb-media" role="img" aria-label="Editing suite with monitors and control desk" style="background:linear-gradient(135deg,#2d3438,#5a6670 60%,#1d2326)"></div>
  </article>
  <article class="thumb-card" style="left:430px">
    <h3 class="display">Motion Graphics</h3>
    <div class="thumb-media" role="img" aria-label="Title card artwork for a television series" style="background:linear-gradient(135deg,#c8742f,#e3a765 50%,#8a4a25)"></div>
  </article>
  <article class="thumb-card" style="left:820px">
    <h3 class="display">Color Correction</h3>
    <div class="thumb-media" role="img" aria-label="Graded film still in cool grey tones" style="background:linear-gradient(135deg,#5d6464,#b8bcbb 50%,#454b4b)"></div>
  </article>
</section>
<svg class="chevron" viewBox="0 0 1200 100" preserveAspectRatio="none">
  <polygon points="0,0 1200,0 1200,40 600,100 0,40" fill="#154a47"/>
  <polygon points="0,40 600,100 1200,40 1200,48 600,108 0,48" fill="#2f8f86"/>
</svg>

<div class="section-label" style="top:1050px"><h2 class="display">Post-Production</h2></div>
<section class="service" style="top:1116px">
  <div class="service-body">
    <div class="service-head"><h3>Secondary Heading</h3><span class="project">Project Title</span></div>
    <p>Every project starts in the edit bay. We log, sort and cut your footage into a clear story, then add sound, titles and finishing touches. Our editors work closely with you from the first assembly to the final master, so each revision stays on schedule and on budget.</p>
    <p>We handle documentaries, brand films and event coverage with the same care. Delivery files are prepared for web, broadcast and cinema screens, and every project is archived safely for future use.</p>
    <a class="more" href="#">Continue Reading...</a>
  </div>
  <div class="service-media" role="img" aria-label="Edit suite with racks of monitors" style="background:linear-gradient(135deg,#3a3f3a,#7c8376 50%,#24282a)"></div>
</section>

<div class="section-label" style="top:1420px"><h2 class="display">Motion Graphics</h2></div>
<section class="service" style="top:1486px">
  <div class="service-media" role="img" aria-label="Animated metallic title artwork on a dark background" style="background:linear-gradient(135deg,#1d2326,#6d7479 50%,#2a1815)"></div>
  <div class="service-body bordered">
    <div class="service-head"><h3>Secondary Heading</h3><span class="project">Project Title</span></div>
    <p>Titles, lower thirds and animated logos give a film its voice. Our designers build motion packages that match your brand and move with purpose, from quick social clips to full opening sequences for a series.</p>
    <p>We deliver clean templates your team can reuse, along with broadcast safe renders and transparent files for any editing system you use in house.</p>
    <a class="more" href="#">Continue Reading...</a>
  </div>
</section>

<div class="section-label" style="top:1790px"><h2 class="display">Color Correction</h2></div>
<section class="service" style="top:1856px">
  <div class="service-body">
    <div class="service-head"><h3>Secondary Heading</h3><span class="project">Project Title</span></div>
    <p>Good colour turns footage into a film. We balance every shot, match cameras and build a look that fits the mood of your story, whether that is a natural daylight feel or a bold stylised grade for drama.</p>
    <p>Our grading suite is calibrated for accurate results across screens. You can join a session in person or review graded stills online before the final render.</p>
    <a class="more" href="#">Continue Reading...</a>
  </div>
  <div class="service-media" role="img" aria-label="Film still of an actor in period costume, warm grade" style="background:linear-gradient(135deg,#4a4a33,#9a8f67 50%,#3a3425)"></div>
</section>

<footer class="site-footer">
  <nav class="footer-nav">
    <a class="active" href="#">Home</a><a href="#">About Us</a><a href="#">Films</a><a href="#">Services</a><a href="#">News &amp; Events</a><a href="#">Contact Us</a>
  </nav>
  <div class="social"><span></span><span></span><span></span><span></span><span></span><span></span></div>
  <div class="newsletter">
    <h4>Join Our Newsletter</h4>
    <div class="newsletter-row"><span>Enter your email address</span><b>JOIN</b></div>
  </div>
  <p class="legal">Quiet Fern Studios<small>Copyright 2024. All rights reserved.</small></p>
</footer>

</body>
</html>
```